GLENMARK VODKA LABELS DESIGN*

we Need a New label for Premium vodka "Velmora Vodka" we are attaching design of current bottle and we need to change logo to Glenmark vodka with completely new design and concept . Please not that current logo is there just for example"

EXACT SIZE AND SHAPE OF LOGO ATTACHED

Logo Text

"glenmark vodka

```html
<!DOCTYPE html>
<html lang="en">
<head>
<meta charset="utf-8">
<title>Velmora Vodka Label</title>
<link href="https://fonts.googleapis.com/css2?family=Montserrat:wght@600;700;800&display=swap" rel="stylesheet">
<style>
  :root {
    --navy: #14213d;
    --rim: #c9a42a;
    --white: #ffffff;
    --backdrop: #f3f3f3;
  }
  html, body {
    margin: 0;
    padding: 0;
    overflow: hidden;
  }
  .canvas {
    position: relative;
    width: 1200px;
    height: 901px;
    overflow: hidden;
    background: radial-gradient(ellipse at 38% 45%, #ffffff 0%, var(--backdrop) 70%);
    font-family: "Montserrat", sans-serif;
  }
  .label {
    position: absolute;
    left: 0;
    top: 0;
    width: 1200px;
    height: 901px;
  }
  .label-text {
    font-family: "Montserrat", sans-serif;
    fill: var(--navy);
  }
  .arch-caption { font-size: 17px; font-weight: 600; letter-spacing: 1.5px; }
  .brand-name { font-size: 58px; font-weight: 800; }
  .spec { font-size: 17px; font-weight: 700; }
  .ribbon-caption { font-size: 17px; font-weight: 700; letter-spacing: 3px; fill: var(--white); }
</style>
</head>
<body>
<div class="canvas">
  <svg class="label" viewBox="0 0 1200 901" xmlns="http://www.w3.org/2000/svg">
    <defs>
      <linearGradient id="gold-foil" x1="0" y1="0" x2="1" y2="0">
        <stop offset="0" stop-color="#c9a32a"/>
        <stop offset="0.3" stop-color="#f5e08a"/>
        <stop offset="0.55" stop-color="#e6c650"/>
        <stop offset="0.8" stop-color="#f2db7c"/>
        <stop offset="1" stop-color="#c19b25"/>
      </linearGradient>
      <path id="arch-curve" d="M352,262 Q457,196 562,262"/>
      <path id="ribbon-curve" d="M326,632 Q457,610 588,632" fill="none"/>
    </defs>

    <path class="shield-rim" d="M307,270 H330 C340,235 390,212 457,212 C525,212 575,235 585,270 H607 V520 C607,590 520,630 457,655 C394,630 307,590 307,520 Z"
          fill="none" stroke="var(--rim)" stroke-width="16" stroke-linejoin="round"/>
    <path class="shield" d="M307,270 H330 C340,235 390,212 457,212 C525,212 575,235 585,270 H607 V520 C607,590 520,630 457,655 C394,630 307,590 307,520 Z"
          fill="url(#gold-foil)" stroke="var(--navy)" stroke-width="3.5" stroke-linejoin="round"/>
    <line class="arch-divider" x1="330" y1="270" x2="585" y2="270" stroke="var(--navy)" stroke-width="3"/>

    <text class="label-text arch-caption" text-anchor="middle">
      <textPath href="#arch-curve" startOffset="50%">MADE IN AMERICA</textPath>
    </text>

    <rect class="crown" x="416" y="278" width="82" height="44" rx="6" fill="var(--navy)" role="img" aria-label="Crown emblem"/>

    <polygon class="star" fill="var(--white)" points="381,289 384,296 391,296 385.5,300.5 387.5,307.5 381,303 374.5,307.5 376.5,300.5 371,296 378,296"/>
    <polygon class="star" fill="var(--white)" points="533,289 536,296 543,296 537.5,300.5 539.5,307.5 533,303 526.5,307.5 528.5,300.5 523,296 530,296"/>

    <text class="label-text brand-name" x="457" y="410" text-anchor="middle">Velmora</text>
    <text class="label-text brand-name" x="457" y="486" text-anchor="middle">Vodka</text>

    <text class="label-text spec" x="402" y="571" text-anchor="middle">1000ML</text>
    <text class="label-text spec" x="517" y="571" text-anchor="middle">38% VOL</text>

    <path class="ribbon-tail" d="M326,618 L272,636 L294,647 L278,664 L334,652 Z" fill="var(--navy)" stroke="var(--rim)" stroke-width="3" stroke-linejoin="round"/>
    <path class="ribbon-tail" d="M588,618 L642,636 L620,647 L636,664 L580,652 Z" fill="var(--navy)" stroke="var(--rim)" stroke-width="3" stroke-linejoin="round"/>
    <path class="ribbon" d="M316,608 Q457,584 598,608 L598,644 Q457,620 316,644 Z" fill="var(--navy)" stroke="var(--rim)" stroke-width="3" stroke-linejoin="round"/>
    <text class="label-text ribbon-caption" text-anchor="middle">
      <textPath href="#ribbon-curve" startOffset="50%">PREMIUM QUALITY</textPath>
    </text>
  </svg>
</div>
</body>
</html>
```